M&A Advisory firm needs elegant and powerful letterhead

We need a powerful but elegant letterhead to engage with the international financial industry.

Target Market(s)

New York and International Financial Industry

Industry/Entity Type

Finance

Font styles to use
Other font styles liked:
• Poppins

Requirements
Must have
• 437 W 82nd Street 14th Floor New York, NY 10024 O: +1 (212) 555 0147 F: +1 (212) 555 0182

```html
<!DOCTYPE html>
<html lang="en">
<head>
<meta charset="utf-8">
<title>Meridane Letterhead</title>
<link rel="stylesheet" href="https://fonts.googleapis.com/css2?family=Open+Sans:wght@400&family=Poppins:wght@500&display=swap">
<style>
  :root {
    --backdrop: #e3e5e5;
    --paper: #ffffff;
    --brand-blue: #0a5697;
    --band-grey: #858585;
    --ink: #1a1a1a;
  }
  * { margin: 0; padding: 0; box-sizing: border-box; }
  html, body {
    width: 1200px;
    height: 686px;
    overflow: hidden;
    background: var(--backdrop);
  }
  .letterhead {
    position: absolute;
    left: 374px;
    top: 23px;
    width: 452px;
    height: 640px;
    background: var(--paper);
    box-shadow: 0 4px 18px rgba(0, 0, 0, 0.14);
    overflow: hidden;
  }
  .letterhead__frame {
    position: absolute;
    inset: 0;
  }
  .brand {
    position: absolute;
    left: 36px;
    top: 30px;
    display: flex;
    align-items: center;
    gap: 8px;
  }
  .brand__dot {
    width: 14px;
    height: 14px;
    border-radius: 50%;
    background: var(--brand-blue);
  }
  .brand__name {
    font-family: "Poppins", sans-serif;
    font-weight: 500;
    font-size: 24px;
    letter-spacing: 1px;
    color: var(--brand-blue);
    line-height: 1;
  }
  .contact {
    position: absolute;
    right: 34px;
    bottom: 30px;
    font-family: "Open Sans", sans-serif;
    font-style: normal;
    font-size: 10px;
    line-height: 1.35;
    color: var(--ink);
    text-align: right;
  }
  .contact__item {
    display: flex;
    justify-content: flex-end;
    align-items: flex-start;
    gap: 8px;
  }
  .contact__item + .contact__item { margin-top: 3px; }
  .contact__icon {
    width: 10px;
    height: 10px;
    flex: none;
    margin-top: 2px;
  }
</style>
</head>
<body>
  <main class="letterhead">
    <svg class="letterhead__frame" width="452" height="640" viewBox="0 0 452 640" aria-hidden="true">
      <rect class="edge-band" x="0" y="0" width="12" height="640" fill="var(--band-grey)"/>
      <polygon class="corner-band" points="0,496 0,640 106,640" fill="var(--band-grey)"/>
      <polygon class="corner-accent corner-accent--bottom" points="0,528 0,640 90,640" fill="var(--brand-blue)"/>
      <polygon class="corner-accent corner-accent--top" points="384,0 452,0 452,58" fill="var(--brand-blue)"/>
    </svg>

    <header class="brand">
      <span class="brand__dot"></span>
      <span class="brand__name">Meridane</span>
    </header>

    <address class="contact">
      <div class="contact__item">
        <span>437 W 82nd Street 14th Floor<br>New York, NY 10024</span>
        <svg class="contact__icon" viewBox="0 0 10 10" aria-label="Address">
          <path d="M5 0.5a3.2 3.2 0 0 0-3.2 3.2C1.8 6 5 9.5 5 9.5s3.2-3.5 3.2-5.8A3.2 3.2 0 0 0 5 0.5z" fill="var(--brand-blue)"/>
          <circle cx="5" cy="3.7" r="1.2" fill="#fff"/>
        </svg>
      </div>
      <div class="contact__item">
        <span>+1 (212) 555 0147</span>
        <svg class="contact__icon" viewBox="0 0 10 10" aria-label="Phone">
          <path d="M2.2 0.8l1.6 1.9-0.9 1.2c0.6 1.3 1.6 2.3 2.9 2.9l1.2-0.9 1.9 1.6-1 1.6C4.4 9.1 0.9 5.6 0.6 1.8z" fill="var(--brand-blue)"/>
        </svg>
      </div>
      <div class="contact__item">
        <span>+1 (212) 555 0182</span>
        <svg class="contact__icon" viewBox="0 0 10 10" aria-label="Fax">
          <rect x="2.5" y="0.8" width="5" height="3" fill="none" stroke="var(--brand-blue)" stroke-width="0.9"/>
          <rect x="0.8" y="3.6" width="8.4" height="5.6" rx="0.8" fill="var(--brand-blue)"/>
          <rect x="2.5" y="5.2" width="5" height="1" fill="#fff"/>
        </svg>
      </div>
    </address>
  </main>
</body>
</html>
```